Double Gate Fold Brochure for Medical Center

We need an elegant design for a double-gate fold brochure for a medical center.
- Logo is attached
- Output must be in .AI format
- Brand colors is gold/light brown, as used in the logo
- The print template for 14"x 8.5" double-gate brochure is attached. (zip)
- Below is a link to content and images. Please be creative about the layouts, effect and placements.

https://slides.vornatek.net/deck/q/7Qv-2KmT_w9XrLp0aZc3HhE5nYbU4sJdFgMi1oRtS8y/open?mode=sharing

```html
<!DOCTYPE html>
<html lang="en">
<head>
<meta charset="utf-8">
<title>Corvale Surgical Institute – Brochure</title>
<link href="https://fonts.googleapis.com/css2?family=Libre+Baskerville&family=Lora:wght@400;500&display=swap" rel="stylesheet">
<style>
:root{
  --gold:#b8a27a;
  --gold-deep:#9f8a60;
  --title:#8a7349;
  --ink:#3a3a3a;
  --paper:#ffffff;
  --mist:#eef4f3;
  --mint:#dcebe7;
}
*{box-sizing:border-box;margin:0;padding:0}
html,body{width:1200px;height:729px;overflow:hidden;background:var(--paper)}
body{font-family:"Lora",Georgia,serif;color:var(--ink);position:relative}
.panel{position:absolute;top:0;height:729px;overflow:hidden}
.title{font-family:"Libre Baskerville",Georgia,serif;color:var(--title);font-weight:400;letter-spacing:1px;text-align:center;line-height:1.05}
.photo{position:absolute;display:block}
.ticks{list-style:none}
.ticks li{position:relative;padding-left:22px;line-height:17px;margin-bottom:4px}
.ticks li::before{content:"✓";position:absolute;left:2px;top:0;color:inherit;font-size:12px}

/* Panel 1 – facility */
.facility{left:0;width:296px;background:linear-gradient(180deg,var(--mist),#fff 60%)}
.facility .title{font-size:26px;position:absolute;top:24px;left:0;width:296px;padding-right:50px}
.facility .intro{position:absolute;top:74px;left:24px;width:245px;font-size:12.2px;line-height:17px;text-align:justify}
.facility .lobby{top:172px;left:0;width:296px;height:193px;background:linear-gradient(160deg,#e9e7e3,#f7f5f1 55%,#c9b79a)}
.facility .features{position:absolute;top:365px;left:0;width:296px;height:192px;background:var(--gold);color:#fff;padding:14px 10px 0 22px;font-size:12.4px}
.facility .features h3{font-weight:400;font-size:12.6px;margin-bottom:4px}
.facility .recovery{top:557px;left:0;width:296px;height:172px;background:linear-gradient(170deg,#f1f1f1,#e2e2e0 60%,#cfc9bf)}

/* Panel 2 – equipment */
.equipment{left:296px;width:304px;background:linear-gradient(180deg,var(--mist),#fff 45%)}
.equipment .title{font-size:26px;position:absolute;top:24px;left:0;width:304px;padding-right:60px}
.equipment .lead{position:absolute;top:66px;left:25px;width:270px;font-size:12.2px;line-height:17px;font-weight:500}
.equipment .ticks{position:absolute;top:104px;left:22px;width:275px;font-size:12.4px;color:var(--ink)}
.equipment .ticks li::before{color:var(--gold)}
.equipment .or-suite{top:463px;left:0;width:304px;height:266px;background:linear-gradient(180deg,#d9dee0,#eef0f0 55%,#c6cacc)}

/* Panel 3 – hospitality */
.hospitality{left:600px;width:306px;background:var(--gold-deep)}
.hospitality .room{top:0;left:0;width:306px;height:195px;background:linear-gradient(160deg,#eef1f3,#dcdcd8 60%,#b79a72)}
.hospitality .title{font-size:28px;color:#fff;position:absolute;top:200px;left:0;width:306px}
.hospitality .ticks{position:absolute;top:244px;left:26px;width:270px;color:#fff;font-size:12.4px}
.brand{position:absolute;top:600px;left:0;width:306px;text-align:center;color:#fff}
.brand .mark{display:block;font-family:"Libre Baskerville",Georgia,serif;font-size:34px;line-height:1;margin-bottom:26px}
.brand .sub{font-family:"Libre Baskerville",Georgia,serif;font-size:10px;letter-spacing:.6px}

/* Panel 4 – physician advantage */
.advantage{left:906px;width:294px;background:linear-gradient(160deg,#f3f7f6,var(--mint) 55%,#eaf2ef)}
.advantage .title{font-size:29px;position:absolute;top:10px;left:0;width:294px;padding-left:14px}
.advantage .lead{position:absolute;top:74px;left:19px;font-size:12.4px;font-weight:500}
.advantage .specialties{position:absolute;top:92px;left:19px;font-size:12.4px}
.advantage .specialties li{margin-bottom:1.6px}
.advantage .specialties li::before,.advantage .terms li::before{color:var(--gold)}
.advantage .program{position:absolute;top:360px;left:19px;width:262px;font-size:12.4px;line-height:18px}
.advantage .terms{position:absolute;top:418px;left:19px;font-size:12.4px}
.advantage .terms li{margin-bottom:1.4px}
.contact-band{position:absolute;top:540px;left:0;width:294px;height:189px;background:var(--gold-deep)}
.portrait{top:517px;left:98px;width:96px;height:117px;border-radius:0 14px 0 14px;background:linear-gradient(180deg,#8fa0ab,#5a6670)}
.contact{position:absolute;top:637px;left:0;width:294px;text-align:center;color:#fff;font-size:11.2px;line-height:14px}
.contact .name{font-size:12px;font-weight:500}
.contact .gap{height:8px}
.contact .note{font-size:6.8px;line-height:8px;margin-top:7px}
</style>
</head>
<body>

<section class="panel facility">
  <h2 class="title">FACILITY</h2>
  <p class="intro">Established in 2017 and Accredited by NCAS-HC, Corvale Surgical Institute is strategically located in heart of South Bayat one of the most prestigious buildings in the area.</p>
  <div class="photo lobby" role="img" aria-label="Bright reception lobby with white curved desk and wood ceiling"></div>
  <div class="features">
    <h3>Our 14,000 Sq Ft. Facility Includes:</h3>
    <ul class="ticks">
      <li>4 Integrated Operating Rooms Equipped With Latest Technology</li>
      <li>8 Private Recovery Rooms With Over night Stay</li>
      <li>Luxurious Reception Area</li>
      <li>Physician Lounge &amp; Pantry</li>
      <li>Spacious Recreational Outdoor Patio</li>
    </ul>
  </div>
  <div class="photo recovery" role="img" aria-label="Recovery bay with beds and curtains"></div>
</section>

<section class="panel equipment">
  <h2 class="title">EQUIPMENT</h2>
  <p class="lead">We Are Proud To Offer Our Physicians The Latest In Surgical Technology:</p>
  <ul class="ticks">
    <li>Integrated Laparoscopic Equipment</li>
    <li>5k Resolution Camera Head</li>
    <li>4k, 32" Boom Monitors</li>
    <li>Onsite Radiology &amp; Fluoroscopy</li>
    <li>Integrated Endoscopy Suite</li>
    <li>ClearView Video Laryngoscope</li>
    <li>Fiberoptic Laryngoscope</li>
    <li>Veltrix A6 Portable Ultrasound</li>
    <li>Advanced Laparoscopic And Arthroscopic Instruments</li>
    <li>Aquila Flow Suction/ Irrigation Systems</li>
    <li>Central Gas System</li>
    <li>Hospital Grade Beds In Recovery Rooms</li>
    <li>Fully Implemented Emr</li>
    <li>Onsite Dictation Software</li>
  </ul>
  <div class="photo or-suite" role="img" aria-label="Operating room with surgical table, lights and boom monitors"></div>
</section>

<section class="panel hospitality">
  <div class="photo room" role="img" aria-label="Private recovery room with bed and armchair"></div>
  <h2 class="title">HOSPITALITY</h2>
  <ul class="ticks">
    <li>8 Private Recovery Rooms Equipped With Hospital Grade Beds And Cable Tv And Apps</li>
    <li>Overnight And Extended Stay Capability For Patient Comfort</li>
    <li>24/7 Support Staff</li>
    <li>Transfer Agreement With An Advanced Closeby Hospital</li>
    <li>Dedicated Physician Liaison</li>
    <li>Complimentary Stay For Physicians And Patients At The Next-door Harborline Hotel</li>
    <li>Courtesy Transportations To/from Facility For Surgeons And Patients</li>
    <li>Free Parking For Physicians, Staff, Patients And Families.</li>
    <li>Walking Distance To Westbay Shopping Center, Hotels And Restaurants</li>
  </ul>
  <div class="brand">
    <span class="mark">Corvale</span>
    <span class="sub">SURGICAL INSTITUTE</span>
  </div>
</section>

<section class="panel advantage">
  <h2 class="title">PHYSICIAN<br>ADVANTAGE</h2>
  <p class="lead">Corvale is your facility of choice for</p>
  <ul class="ticks specialties">
    <li>General Surgery</li>
    <li>Bariatric Surgery</li>
    <li>Gynecology</li>
    <li>Urology</li>
    <li>Orthopedics</li>
    <li>Spine Surgery</li>
    <li>Pain management</li>
    <li>Plastic &amp; Reconstructive</li>
    <li>Hand Surgery</li>
    <li>Pediatric Surgery</li>
    <li>Podiatric Surgery</li>
    <li>Head and Neck Surgery</li>
    <li>ENT</li>
    <li>Colon &amp; Rectal Surgery</li>
  </ul>
  <p class="program">Our “Physician Partnership Program” are structured by one of the most respected healthcare law firms in SoCal</p>
  <ul class="ticks terms">
    <li>No Buy-In required</li>
    <li>No Non-Compete Clause</li>
    <li>No Long-Term Commitment</li>
    <li>Guaranteed Membership Status</li>
    <li>No-membership fee</li>
  </ul>
  <div class="contact-band"></div>
  <div class="photo portrait" role="img" aria-label="Portrait of the director of operation"></div>
  <div class="contact">
    <div class="name">Daniel Marsoni, MBA</div>
    <div>Director of Operation</div>
    <div class="gap"></div>
    <div>310 555 0147</div>
    <div>daniel.m@corvalesurgical.com</div>
    <p class="note">For more information about Physician Partnership<br>Programs, please contact:</p>
  </div>
</section>

</body>
</html>
```